Stationary and design update for my brand

I need new letterhead, a new business card, business envelope design, new keynote and powerpoint branded slides (16x9). I have logo samples in various styles and brand standards for fonts and colors.

Font styles to use
Sans Serif

```html
<!DOCTYPE html>
<html lang="en">
<head>
<meta charset="utf-8">
<title>Ridgeline Business Card</title>
<link rel="stylesheet" href="https://fonts.googleapis.com/css2?family=Arimo:wght@400;700&display=swap">
<style>
  :root {
    --orange: #f89c35;
    --orange-deep: #f28a33;
    --ink: #7b7b7e;
    --paper: #ffffff;
    --edge: #1a1a1a;
  }
  * { margin: 0; padding: 0; box-sizing: border-box; }
  html, body {
    width: 1200px; height: 1200px; overflow: hidden;
    background: var(--paper);
    font-family: "Arimo", Arial, sans-serif;
  }
  .sheet { position: relative; width: 1200px; height: 1200px; }
  .card {
    position: absolute; left: 194px; width: 819px; height: 499px;
    border: 1px solid var(--edge);
    overflow: hidden;
  }
  .card--front { top: 93px; background: var(--paper); padding: 2px; }
  .card--front .face { position: relative; width: 100%; height: 100%; background: var(--orange); }
  .card--back { top: 627px; background: var(--paper); }

  .brand-name {
    position: absolute; white-space: nowrap;
    font-weight: 700; letter-spacing: 2px; line-height: 1;
  }
  .card--front .brand-name {
    left: 0; width: 100%; padding-left: 420px; top: 262px;
    font-size: 42px; color: var(--paper);
  }
  .front-email {
    position: absolute; left: 0; width: 100%; padding-left: 420px; top: 324px;
    text-align: left; font-size: 21px; color: var(--orange-deep);
    white-space: nowrap;
  }

  .person-name {
    position: absolute; left: 49px; top: 132px;
    font-size: 36px; font-weight: 700; color: var(--ink); line-height: 1; white-space: nowrap;
  }
  .person-name .credentials { font-size: 19px; font-weight: 400; }
  .name-rule {
    position: absolute; left: 50px; top: 175px; width: 64px; height: 4px;
    background: var(--orange);
  }
  .role {
    position: absolute; left: 49px; top: 185px;
    font-size: 24px; line-height: 26px; color: var(--ink);
  }
  .contacts { position: absolute; left: 50px; top: 306px; list-style: none; }
  .contact {
    display: flex; align-items: flex-start; gap: 13px;
    font-size: 19px; line-height: 20px; color: var(--ink);
    margin-bottom: 10px;
  }
  .contact .icon {
    flex: none; width: 31px; height: 31px; border-radius: 50%;
    background: var(--ink); display: flex; align-items: center; justify-content: center;
  }
  .contact .text { padding-top: 6px; }
  .card--back .brand-name {
    left: 555px; top: 388px; font-size: 40px; color: var(--orange);
  }
</style>
</head>
<body>
<main class="sheet">
  <section class="card card--front" aria-label="Card front">
    <div class="face">
      <div class="brand-name">RIDGELINE</div>
      <div class="front-email">daniel@ridgelinecbc.com</div>
    </div>
  </section>

  <section class="card card--back" aria-label="Card back">
    <h1 class="person-name">Daniel Okafor-Lindqvist<span class="credentials">,DMIN, PCC</span></h1>
    <div class="name-rule"></div>
    <p class="role">Owner / Trainer / Coach / Consultant<br>Ridgeline Coaching and Behavioral<br>Consulting LLC</p>

    <ul class="contacts">
      <li class="contact">
        <span class="icon">
          <svg width="17" height="17" viewBox="0 0 24 24" fill="#fff"><path d="M6.6 10.8a15 15 0 0 0 6.6 6.6l2.2-2.2c.3-.3.7-.4 1-.2 1.1.4 2.3.6 3.6.6.6 0 1 .4 1 1V20c0 .6-.4 1-1 1A17 17 0 0 1 3 4c0-.6.4-1 1-1h3.5c.6 0 1 .4 1 1 0 1.3.2 2.5.6 3.6.1.3 0 .7-.2 1z"/></svg>
        </span>
        <span class="text">Cell: (555) 014-2290</span>
      </li>
      <li class="contact">
        <span class="icon">
          <svg width="18" height="18" viewBox="0 0 24 24" fill="none" stroke="#fff" stroke-width="1.6"><circle cx="12" cy="12" r="9"/><ellipse cx="12" cy="12" rx="4" ry="9"/><path d="M3 12h18M4.5 7.5h15M4.5 16.5h15"/></svg>
        </span>
        <span class="text">daniel@ridgelinecbc.com</span>
      </li>
      <li class="contact">
        <span class="icon">
          <svg width="16" height="16" viewBox="0 0 24 24" fill="#fff"><path d="M12 2a7 7 0 0 0-7 7c0 5 7 13 7 13s7-8 7-13a7 7 0 0 0-7-7zm0 9.5A2.5 2.5 0 1 1 12 6.5a2.5 2.5 0 0 1 0 5z"/></svg>
        </span>
        <span class="text">4820 Alder Crest Ln.<br>Brookfield, TX 75000</span>
      </li>
    </ul>

    <div class="brand-name">RIDGELINE</div>
  </section>
</main>
</body>
</html>
```